Annual Report Belvora 2025

Take a PowerPoint presentation and turn it into a info graphic type annual report, posters and flyers.

Annual report ideally no more than 8 pages.

Please use the colours and fonts in the attached brand guidelines.

We are looking for an infographic visually appealing piece.

```html
<!DOCTYPE html>
<html lang="en">
<head>
<meta charset="UTF-8">
<title>Belvora 2025 Annual Report — Cover</title>
<link rel="stylesheet" href="https://fonts.googleapis.com/css2?family=Roboto:wght@400;700;900&display=swap">
<style>
  :root {
    --backdrop: #4d4d4d;
    --navy: #002b57;
    --green: #7aa32b;
    --white: #ffffff;
    --photo-warm: #d8c4ae;
    --photo-cool: #5c6f8a;
  }
  html, body {
    margin: 0;
    padding: 0;
    width: 1200px;
    height: 1001px;
    overflow: hidden;
    background: var(--backdrop);
    font-family: "Roboto", Arial, sans-serif;
  }
  .cover {
    position: absolute;
    left: 62px;
    top: 198px;
    width: 1075px;
    height: 606px;
  }
  .cover-panel {
    position: absolute;
    left: 0;
    top: 0;
    width: 560px;
    height: 606px;
    background: var(--navy);
  }
  .cover-photo {
    position: absolute;
    left: 560px;
    top: -2px;
    width: 515px;
    height: 608px;
    background: linear-gradient(135deg, #efe6da 0%, var(--photo-warm) 40%, #8a97ad 70%, var(--photo-cool) 100%);
  }
  .accent-bar {
    position: absolute;
    left: 552px;
    top: 84px;
    width: 16px;
    height: 438px;
    background: var(--green);
  }
  .brand {
    position: absolute;
    left: 98px;
    top: 104px;
    display: flex;
    align-items: center;
    gap: 10px;
    color: var(--white);
    font-weight: 700;
    font-size: 34px;
    letter-spacing: 0.2px;
  }
  .brand-dot {
    width: 24px;
    height: 24px;
    border-radius: 50%;
    background: var(--green);
  }
  .report-title {
    position: absolute;
    left: 86px;
    top: 172px;
    margin: 0;
    color: var(--white);
    font-weight: 700;
    font-size: 72px;
    line-height: 64px;
    letter-spacing: -0.5px;
  }
  .report-theme {
    position: absolute;
    left: 87px;
    top: 370px;
    margin: 0;
    color: var(--green);
    font-weight: 400;
    font-size: 24px;
    line-height: 25px;
  }
  .contact {
    position: absolute;
    left: 88px;
    top: 440px;
    margin: 0;
    color: var(--white);
    font-size: 13.5px;
    line-height: 19px;
  }
  .website {
    position: absolute;
    left: 88px;
    top: 503px;
    margin: 0;
    color: var(--green);
    font-weight: 700;
    font-size: 14px;
  }
</style>
</head>
<body>
  <div class="cover">
    <section class="cover-panel">
      <div class="brand"><span class="brand-dot"></span>Belvora</div>
      <h1 class="report-title">2025<br>ANNUAL<br>REPORT</h1>
      <p class="report-theme">Resilience Through Partnership<br>&nbsp;Values Driving Value</p>
      <p class="contact">18 Alder Lane West, Kitchener, ON N2B 4K7<br>Charitable Registration #: 71452 3390 Rr0001</p>
      <p class="website">belvora.ca</p>
    </section>
    <div class="cover-photo" role="img" aria-label="Photograph of a smiling senior couple, the woman standing behind the seated man with her hands on his shoulders"></div>
    <div class="accent-bar"></div>
  </div>
</body>
</html>
```